Book cover: Stormy Days Survival for Kids (A5)

I have a book called Stormy Days Survival for Teens. It is a book for teenagers which gives them tips and tactics on how to survive life's challenges regarding friends, family, feelings, relationships and hard stuff in life generally. I will upload the cover of this book but you can see it on my past jobs as one of the designers her eon Pixel Bazaar did it for me.
I have a new book I've written called Stormy Days Survival for Kids. This is a parallel book to Stormy Days Survival for Teens, but it is specifically for 8 to 12 or 13 year olds, rather than for older teens.
A very important aspect of this job is that it SHOULD MATCH in some strong way - the Stormy Days Survival for Teens book. I will be selling them together, displaying them together and I want them to look like two of a pair. It might be that you use the same image as the first book but change the colour of the image so that it is bright orange and green perhaps? Or that there is another image but in the image is placed in the exact same position across the book as the first book. It needs to look like the books are by the same author.
However, I would like this one to look a bit "younger", more kid friendly. For example, a font that looks like it is for kids, or kids' writing perhaps.
I dont want to have photos on the book, and I dont think I want cartoons or drawings - because I'm not sure how this will tie in with the first book.
I want it to look modern, fresh and designed specifically for kids. The text needs to be:
Stormy Days Survival - For Kids!
Tips and ideas for 8 to 13 year olds about how to stay cool, calm and confident on even the toughest days!
The back cover is going to mostly just have the table of contents listed and a blurb, with one or two cartoons which I will supply. I am keen to pick a designer to just do the front cover first and will ask them to do the back cover later.
UPDATED: I have attached three files with fonts that I like.

```html
<!DOCTYPE html>
<html lang="en">
<head>
<meta charset="utf-8">
<title>Stormy Days Survival for Kids – Cover Spread</title>
<link href="https://fonts.googleapis.com/css2?family=Anton&family=Fredoka:wght@500&family=Oswald:wght@500;700&family=Libre+Baskerville&display=swap" rel="stylesheet">
<style>
  :root {
    --page-bg: #ffffff;
    --cover-cream: #f4f2c2;
    --flourish: #f9f8df;
    --band-brown: #bf9a5e;
    --panel-white: #ffffff;
    --title-red: #e2402d;
    --ink: #1c1c1c;
    --spine-edge: #e6e3ad;
  }
  * { box-sizing: border-box; margin: 0; padding: 0; }
  html, body {
    width: 1200px; height: 1000px; overflow: hidden;
    background: var(--page-bg);
  }
  body { position: relative; }
  .spread {
    position: absolute; left: 15px; top: 30px;
    width: 1170px; height: 940px;
    display: flex; overflow: hidden;
    background: var(--cover-cream);
  }
  .back-cover, .front-cover { position: relative; width: 540px; height: 100%; overflow: hidden; }
  .spine {
    position: relative; width: 90px; height: 100%; overflow: hidden;
    border-left: 1px solid var(--spine-edge);
    border-right: 1px solid var(--spine-edge);
  }

  .flourish {
    position: absolute; background: var(--flourish); border-radius: 40px; opacity: .9;
  }
  .back-cover .flourish--top { left: 120px; top: 20px; width: 340px; height: 150px; }
  .back-cover .flourish--bottom { left: 0; top: 730px; width: 300px; height: 200px; }
  .front-cover .flourish--top { left: 20px; top: 20px; width: 400px; height: 200px; }
  .front-cover .flourish--bottom { left: 20px; top: 720px; width: 260px; height: 200px; }

  .band { position: absolute; left: 0; right: 0; }
  .band__line { display: block; background: var(--band-brown); }
  .band__line--thin { height: 4px; margin-bottom: 4px; }
  .band__line--thick { height: 8px; }
  .band--upper { top: 254px; }
  .band--lower { top: 662px; }
  .band--lower .band__line--thick { margin-bottom: 4px; }

  .title-panel {
    position: absolute; left: 0; right: 0; top: 270px; height: 392px;
    background: var(--panel-white);
    padding: 30px 16px 0 16px;
    overflow: hidden;
  }
  .title {
    display: flex; align-items: flex-start; gap: 12px;
    color: var(--title-red);
    font-family: "Anton", "Impact", sans-serif; font-weight: 400;
    text-transform: uppercase; line-height: .98;
  }
  .title__left { font-size: 58px; padding-top: 14px; }
  .title__right { display: flex; flex-direction: column; }
  .title__main { font-size: 84px; line-height: 1; }
  .title__tag {
    font-family: "Fredoka", "Arial Rounded MT Bold", sans-serif;
    font-weight: 500; text-transform: none;
    font-size: 44px; line-height: 1; margin-left: 20px; margin-top: 4px;
  }
  .subtitle {
    width: 508px; margin-top: 40px;
    font-family: "Oswald", "Arial Narrow", sans-serif; font-weight: 500;
    font-size: 8px; letter-spacing: 0; color: var(--ink);
    text-transform: uppercase; white-space: nowrap;
  }

  .author { position: absolute; right: 30px; top: 860px; text-align: center; }
  .author__name {
    font-family: "Oswald", "Arial Narrow", sans-serif; font-weight: 700;
    font-size: 28px; color: var(--ink); letter-spacing: .5px;
  }
  .author__role {
    font-family: "Libre Baskerville", Georgia, serif; font-size: 13px; color: var(--ink);
  }

  .spine__title, .spine__author {
    position: absolute; left: 50%; transform: translateX(-50%);
    writing-mode: vertical-rl;
    font-family: "Oswald", "Arial Narrow", sans-serif; font-weight: 700;
    color: var(--ink); text-transform: uppercase; white-space: nowrap;
  }
  .spine__title { top: 285px; font-size: 25px; }
  .spine__author { top: 690px; font-size: 20px; text-align: center; line-height: 1.1; }
  .spine__author small {
    font-family: "Libre Baskerville", Georgia, serif; font-weight: 400;
    font-size: 11px; text-transform: none;
  }
</style>
</head>
<body>
  <main class="spread">
    <section class="back-cover">
      <div class="flourish flourish--top" role="img" aria-label="Soft pale scrolling flourish ornament"></div>
      <div class="flourish flourish--bottom" role="img" aria-label="Soft pale scrolling flourish ornament"></div>
    </section>

    <section class="spine">
      <div class="band band--upper"><span class="band__line band__line--thin"></span><span class="band__line band__line--thick"></span></div>
      <p class="spine__title">Stormy Days Survival - For Kids</p>
      <div class="band band--lower"><span class="band__line band__line--thick"></span><span class="band__line band__line--thin"></span></div>
      <p class="spine__author">Marella Quint<br><small>clinical psychologist</small></p>
    </section>

    <section class="front-cover">
      <div class="flourish flourish--top" role="img" aria-label="Soft pale scrolling flourish ornament"></div>
      <div class="band band--upper"><span class="band__line band__line--thin"></span><span class="band__line band__line--thick"></span></div>
      <div class="title-panel">
        <h1 class="title">
          <span class="title__left">Stormy<br>Days</span>
          <span class="title__right">
            <span class="title__main">Survival</span>
            <span class="title__tag">for kids</span>
          </span>
        </h1>
        <p class="subtitle">Tips and ideas for 8 to 13 years old about how to stay cool, calm and confident even the toughest day</p>
      </div>
      <div class="band band--lower"><span class="band__line band__line--thick"></span><span class="band__line band__line--thin"></span></div>
      <div class="flourish flourish--bottom" role="img" aria-label="Soft pale scrolling flourish ornament"></div>
      <div class="author">
        <p class="author__name">MARELLA QUINT</p>
        <p class="author__role">clinical psychologist</p>
      </div>
    </section>
  </main>
</body>
</html>
```